Velvet Lantern Gala 2014

We're looking to create an 8 1/2" x11" print design using certain elements that we provide.

This is for an invitation/program cover for a Velvet Lantern Gala - so the design has to have a classy look using a set number of colors - GOLD, PURPLE, GREEN - white can also be used as accent or boarder elements.

Please use the file OBVEK 2014 for inspiration and direction. The design MUST connect to that file.

The final design should cause a WOW! factor and play off / or be a companion to design we will upload. (see files)

Requirements
Must have
• Dimension size 8 1/2'' x 11'' (bleed to the end)
St. Augustine Seal to remain (can be small)
A Mardi Gras Mask or person in mask behind front elements which should use transparency
Event location, date, time
Files appropriate for printing - with a semi-transparent object in file
Nice to have
• Key elements like shown on the OBVEK 2014 file
Purple as a key color - either as background or like feathers on picture
10th Annual must show nicely
FONTS: New Century Schoolbook LT and Spinwerad

```html
<!DOCTYPE html>
<html lang="en">
<head>
<meta charset="utf-8">
<title>Velvet Lantern Gala 2014 – Invitation</title>
<link rel="stylesheet" href="https://fonts.googleapis.com/css2?family=Old+Standard+TT:ital,wght@0,400;0,700;1,400&display=swap">
<style>
  :root {
    --plum: #3b3550;
    --gold: #c9981a;
    --silver: #8f8b9c;
    --serif: "Old Standard TT", Georgia, serif;
  }
  html, body { margin: 0; padding: 0; overflow: hidden; background: var(--plum); }
  .invitation {
    position: relative;
    width: 927px;
    height: 1200px;
    overflow: hidden;
    background: var(--plum);
    font-family: var(--serif);
  }
  .mask-art { position: absolute; left: 45px; top: 0; width: 835px; height: 460px; }
  .host {
    position: absolute; left: 0; width: 927px; top: 344px; margin: 0;
    text-align: center; color: var(--gold); font-size: 39px; line-height: 46px;
  }
  .request {
    position: absolute; left: 0; width: 927px; top: 394px; margin: 0;
    text-align: center; color: var(--silver); font-style: italic; font-size: 27px; line-height: 32px;
  }
  .edition {
    position: absolute; left: 45px; top: 467px; margin: 0;
    display: flex; align-items: baseline;
    color: var(--gold); font-weight: 400; line-height: 1; white-space: nowrap;
  }
  .edition .number {
    display: inline-block; font-size: 260px; letter-spacing: -10px;
    transform: scaleX(0.72); transform-origin: left bottom;
  }
  .edition .word {
    display: inline-block; margin-left: -62px; font-size: 127px; letter-spacing: 1px;
    transform: scaleX(0.79); transform-origin: left bottom;
  }
  .edition .word .initial { font-size: 198px; }
  .edition .ordinal {
    position: absolute; left: 167px; top: -12px; font-size: 60px; line-height: 60px;
  }
  .event-name {
    position: absolute; right: 28px; top: 668px; margin: 0;
    color: var(--silver); font-style: italic; font-weight: 400; font-size: 62px; white-space: nowrap;
  }
  .when {
    position: absolute; left: 82px; width: 320px; top: 900px; margin: 0;
    text-align: center; color: var(--gold); font-style: italic; font-size: 36px; line-height: 56px;
  }
  .where {
    position: absolute; left: 0; width: 500px; top: 1072px; margin: 0;
    text-align: center; color: var(--silver); font-style: italic; font-size: 28px; line-height: 37px;
  }
  .school {
    position: absolute; right: 28px; top: 1088px;
    display: flex; align-items: center; gap: 12px;
    color: var(--gold); font-size: 24px; white-space: nowrap;
  }
  .school .dot { width: 30px; height: 30px; border-radius: 50%; background: var(--gold); }
</style>
</head>
<body>
<main class="invitation">
  <svg class="mask-art" viewBox="0 0 835 460" role="img" aria-label="Faint lace masquerade mask behind the heading">
    <defs>
      <radialGradient id="maskGlow" cx="50%" cy="35%" r="60%">
        <stop offset="0%" stop-color="#5e5970" stop-opacity="0.9"/>
        <stop offset="70%" stop-color="#4c4761" stop-opacity="0.6"/>
        <stop offset="100%" stop-color="#3b3550" stop-opacity="0"/>
      </radialGradient>
    </defs>
    <rect x="0" y="0" width="835" height="460" fill="url(#maskGlow)"/>
  </svg>

  <p class="host">The Association of Orchard Bay Alumni</p>
  <p class="request">requests your presence at our</p>

  <h1 class="edition">
    <span class="number">10</span>
    <span class="word"><span class="initial">A</span>NNUAL</span>
    <span class="ordinal">th</span>
  </h1>
  <h2 class="event-name">Velvet Lantern Gala</h2>

  <p class="when">Saturday<br>Febuary 22, 2014<br>7pm-12am</p>

  <p class="where">Linden Harbor Convention Hall<br>480 Marlow Terrace Promenade<br>FAIRHAVEN, GEORGIA</p>

  <div class="school"><span class="dot"></span><span>Orchard Bay Academy</span></div>
</main>
</body>
</html>
```